business card design for luxurious real estate brand

using the attached logo, i am looking for a 2-sided business card design. the back should be the gold logo on black background. the front needs to include: gold logo, name, phone, email, and website

Industry/Entity Type

real estate

Contact Information for Business Card

logo, name, email, phone, website

Font styles to use
Sans Serif

```html
<!DOCTYPE html>
<html lang="en">
<head>
<meta charset="utf-8">
<title>Casa Lumera — Business Card</title>
<link href="https://fonts.googleapis.com/css2?family=Montserrat:wght@500;700&family=Open+Sans:wght@400&display=swap" rel="stylesheet">
<style>
  :root {
    --stage: #2a2a2d;
    --card: #1f1f22;
    --gold: #ffcc12;
    --white: #f4f4f4;
    --shade: #141416;
  }
  * { margin: 0; padding: 0; box-sizing: border-box; }
  html, body { width: 1200px; height: 780px; overflow: hidden; background: var(--stage); }
  .canvas {
    width: 1200px; height: 780px;
    display: flex; flex-direction: column; align-items: center; justify-content: center; gap: 40px;
  }
  .card {
    position: relative;
    width: 600px; height: 343px;
    background: var(--card);
    border-radius: 28px;
    border: 5px solid var(--gold);
    overflow: hidden;
  }
  .brand {
    display: flex; align-items: center; gap: 14px;
    color: var(--gold);
    font-family: "Montserrat", sans-serif; font-weight: 500;
    letter-spacing: 0.22em; text-transform: uppercase;
  }
  .brand-mark { background: var(--gold); flex: none; }

  /* back */
  .card-back { display: flex; align-items: center; justify-content: center; }
  .card-back .brand { font-size: 38px; }
  .card-back .brand-mark { width: 30px; height: 30px; }

  /* front */
  .card-front .brand { position: absolute; left: 44px; top: 112px; font-size: 24px; }
  .card-front .brand-mark { width: 20px; height: 20px; }
  .holder { position: absolute; right: 48px; top: 30px; text-align: right; }
  .holder-name { font-family: "Montserrat", sans-serif; font-weight: 700; font-size: 24px; color: var(--gold); }
  .holder-title { font-family: "Open Sans", sans-serif; font-size: 14px; color: var(--white); margin-top: 2px; }
  .accent-bar { position: absolute; right: 0; top: 30px; width: 26px; height: 36px; background: var(--gold); }
  .decor-block {
    position: absolute; right: 40px; bottom: 30px; width: 170px; height: 150px;
    background: linear-gradient(160deg, #2e2e32, var(--shade));
  }
  .contacts { position: absolute; left: 44px; bottom: 34px; list-style: none; }
  .contacts li {
    display: flex; align-items: center; gap: 10px;
    font-family: "Open Sans", sans-serif; font-size: 15px; color: var(--white);
    line-height: 26px;
  }
  .contacts svg { width: 15px; height: 15px; fill: none; stroke: var(--gold); stroke-width: 2; flex: none; }
</style>
</head>
<body>
<main class="canvas">
  <section class="card card-back">
    <div class="brand"><span class="brand-mark"></span>Casa Lumera</div>
  </section>

  <section class="card card-front">
    <div class="holder">
      <p class="holder-name">Mirela Kostova</p>
      <p class="holder-title">Managing Director</p>
    </div>
    <span class="accent-bar"></span>
    <div class="brand"><span class="brand-mark"></span>Casa Lumera</div>
    <div class="decor-block"></div>
    <ul class="contacts">
      <li>
        <svg viewBox="0 0 24 24"><path d="M5 3h4l2 5-3 2a12 12 0 0 0 6 6l2-3 5 2v4a2 2 0 0 1-2 2A18 18 0 0 1 3 5a2 2 0 0 1 2-2z"/></svg>
        (555) 014-2231
      </li>
      <li>
        <svg viewBox="0 0 24 24"><rect x="2" y="5" width="20" height="14" rx="1"/><path d="M2 6l10 7 10-7"/></svg>
        hello@casalumera.com
      </li>
      <li>
        <svg viewBox="0 0 24 24"><circle cx="12" cy="12" r="10"/><path d="M2 12h20M12 2a15 15 0 0 1 0 20M12 2a15 15 0 0 0 0 20"/></svg>
        www.casalumera.com
      </li>
    </ul>
  </section>
</main>
</body>
</html>
```